Handout postcard for tradeshow

Please create a 2-sided handout postcard for use at a tradeshow. Card should be 4.25" x 5.5"

While postcard sized, a postcard with a place for an address/stamp is not wanted. We want a small handout for a tradeshow for people to take home with them.

The first side should emphasize cost savings.
The second side should emphasize environmental benefits.

The card's design doesn't need to match, but should be in line with the included poster design which will also be used at the tradeshow.

Possible graphics to include are listed below as well as the poster it should emulate.

```html
<!DOCTYPE html>
<html lang="en">
<head>
<meta charset="utf-8">
<title>LoopLane Tradeshow Handout</title>
<link href="https://fonts.googleapis.com/css2?family=Montserrat:wght@400;500;600;700;800&display=swap" rel="stylesheet">
<style>
  :root{
    --green:#3db54a;
    --blue:#22a6e0;
    --sky:#3fc0ec;
    --ink:#2b2b2b;
    --slate:#5a5d62;
    --night-top:#3b5a7c;
    --night-mid:#1c2633;
    --night-low:#121417;
    --forest-a:#1f3a26;
    --forest-b:#3c6a3c;
    --white:#ffffff;
  }
  *{box-sizing:border-box;margin:0;padding:0}
  html,body{width:967px;height:1200px;overflow:hidden;background:var(--white)}
  body{position:relative;font-family:"Montserrat",Arial,sans-serif;color:var(--ink)}
  .card{position:absolute;left:161px;width:644px;height:504px;overflow:hidden;background:var(--white)}
  .card--front{top:76px}
  .card--back{top:619px}

  /* Front */
  .city-photo{position:absolute;left:0;top:0;width:644px;height:331px;
    background:linear-gradient(180deg,var(--night-top) 0%,#5d6f80 30%,var(--night-mid) 55%,var(--night-low) 100%)}
  .headline{position:absolute;left:0;top:232px;width:644px;text-align:center;color:var(--white);
    font-weight:700;font-size:33px;line-height:36px;letter-spacing:-0.3px}
  .front-bands{position:absolute;left:0;top:331px;width:644px;height:173px}
  .join{position:absolute;left:30px;top:345px;color:var(--white);line-height:1}
  .join__lead{font-size:14px;font-weight:400}
  .join__title{font-size:16.5px;font-weight:700;line-height:18px;margin-top:3px;letter-spacing:-0.2px;white-space:nowrap}
  .front-divider{position:absolute;left:179px;top:339px;width:1px;height:70px;background:var(--white)}
  .mission{position:absolute;left:188px;top:346px;width:208px;color:var(--white);
    font-size:8.2px;line-height:11.2px;text-align:justify}
  .brand{position:absolute;font-weight:700;color:var(--slate);display:flex;align-items:center;gap:5px;letter-spacing:-0.5px;white-space:nowrap}
  .brand__dot{width:0.8em;height:0.8em;border-radius:50%;background:var(--blue);display:inline-block;flex:none}
  .brand--front{left:440px;top:352px;font-size:30px;line-height:36px}
  .savings-q{position:absolute;left:30px;top:434px;color:var(--white)}
  .savings-q__title{font-size:17px;font-weight:700;line-height:19px;white-space:nowrap}
  .savings-q__body{font-size:14px;line-height:14px;font-weight:400;margin-top:2px;width:380px}
  .contact{position:absolute;left:445px;top:425px;color:var(--white);font-size:15.5px;font-weight:700;line-height:24px}

  /* Back */
  .forest-photo{position:absolute;left:0;top:0;width:644px;height:280px;
    background:radial-gradient(ellipse at 60% 40%,var(--forest-b) 0%,var(--forest-a) 60%,#14261a 100%)}
  .brand--back{left:48px;top:38px;font-size:27px;line-height:36px;color:var(--white)}
  .using{position:absolute;left:0;top:154px;width:644px;text-align:center;color:var(--white);font-size:17px;font-weight:700}
  .stat{position:absolute;top:178px;color:var(--white)}
  .stat--carbon{left:106px}
  .stat--trucks{left:356px}
  .stat__figure{font-size:36px;font-weight:700;line-height:40px}
  .stat__label{font-size:17px;font-weight:700;line-height:20px}
  .stat-divider{position:absolute;left:321px;top:186px;width:1.5px;height:48px;background:var(--white)}
  .stripe-green{position:absolute;left:0;top:280px;width:644px;height:7px;background:var(--green)}
  .stripe-blue{position:absolute;left:0;top:287px;width:644px;height:10px;background:var(--sky)}
  .badge{position:absolute;top:257px;width:66px;height:66px;border-radius:50%;background:var(--green);
    border:3px solid var(--white);display:flex;align-items:center;justify-content:center}
  .badge svg{width:36px;height:36px}
  .feature{position:absolute;top:328px;width:161px;text-align:center}
  .feature__title{color:var(--green);font-weight:700;font-size:11.5px;line-height:13px;height:30px}
  .feature__text{font-size:8.6px;line-height:12.2px;text-align:justify;text-align-last:center;color:var(--ink)}
  .feature-divider{position:absolute;top:342px;width:1.5px;height:80px;background:var(--green)}
  .footer-band{position:absolute;left:0;top:481px;width:644px;height:23px;background:var(--green)}
</style>
</head>
<body>

<section class="card card--front">
  <div class="city-photo" role="img" aria-label="City skyline at dusk with light trails along a highway"></div>
  <h1 class="headline">CUT YOUR PARCEL COSTS BY<br>10-50%</h1>

  <svg class="front-bands" viewBox="0 0 644 173" aria-hidden="true">
    <polygon points="0,0 388,0 427,82 0,82" fill="var(--green)"/>
    <rect x="0" y="82" width="644" height="1.5" fill="var(--white)"/>
    <polygon points="0,83.5 427,83.5 405,173 0,173" fill="var(--blue)"/>
    <polygon points="427,74 644,74 644,173 405,173" fill="var(--sky)"/>
    <polygon points="427,74 439,74 427,83.5" fill="var(--white)"/>
  </svg>

  <div class="join">
    <div class="join__lead">Join the</div>
    <div class="join__title">GREEN PARCEL<br>MOVEMENT</div>
  </div>
  <div class="front-divider"></div>
  <p class="mission">Our mission is to take the waste out of shipping. Every carrier drives every street in the US daily duplicating each others' routes. We help consolidate routes across carriers using our real-time bidding system for parcels.</p>

  <div class="brand brand--front"><span class="brand__dot"></span>LoopLane</div>

  <div class="savings-q">
    <div class="savings-q__title">HOW MUCH CAN GREEN PARCELS SAVE ME?</div>
    <div class="savings-q__body">Contact us to back-test your parcel data and see how much you could be saving on parcel costs</div>
  </div>
  <div class="contact">info@LoopLane.com<br>www.LoopLane.com</div>
</section>

<section class="card card--back">
  <div class="forest-photo" role="img" aria-label="Aerial view of a dense green forest crossed by a curving road"></div>
  <div class="brand brand--back"><span class="brand__dot"></span>LoopLane</div>

  <div class="using">SEND YOUR PARCELS USING:</div>
  <div class="stat stat--carbon">
    <div class="stat__figure">40% Less</div>
    <div class="stat__label">CARBON EMISSIONS</div>
  </div>
  <div class="stat-divider"></div>
  <div class="stat stat--trucks">
    <div class="stat__figure">25% Less</div>
    <div class="stat__label">TRUCKS ON THE ROAD</div>
  </div>

  <div class="stripe-green"></div>
  <div class="stripe-blue"></div>

  <div class="badge" style="left:91px">
    <svg viewBox="0 0 36 36" fill="none" stroke="#fff" stroke-width="1.6" stroke-linecap="round" stroke-linejoin="round">
      <circle cx="19" cy="13" r="6"/>
      <path d="M19 9.5v7M21 11h-3a1.2 1.2 0 0 0 0 2.4h2a1.2 1.2 0 0 1 0 2.4h-3"/>
      <path d="M4 24h5l5 2h6a1.5 1.5 0 0 1 0 3h-5M9 31l6 1 13-5a1.6 1.6 0 0 0-1.3-3L20 27"/>
      <rect x="2" y="22" width="4" height="10"/>
      <path d="M19 3v2M15 4l1 1.5M23 4l-1 1.5"/>
    </svg>
  </div>
  <div class="badge" style="left:289px">
    <svg viewBox="0 0 36 36" fill="none" stroke="#fff" stroke-width="1.6" stroke-linejoin="round">
      <rect x="7" y="5" width="10" height="11"/>
      <rect x="7" y="17" width="10" height="11"/>
      <rect x="18" y="17" width="10" height="11"/>
      <path d="M10 5v4h4V5M10 17v4h4v-4M21 17v4h4v-4"/>
      <path d="M23 4v9M20 10l3 3 3-3" stroke-linecap="round"/>
      <path d="M4 30h28M6 30v2M30 30v2"/>
    </svg>
  </div>
  <div class="badge" style="left:487px">
    <svg viewBox="0 0 36 36" fill="none" stroke="#fff" stroke-width="1.6" stroke-linejoin="round" stroke-linecap="round">
      <rect x="5" y="9" width="18" height="15"/>
      <path d="M23 13h6l4 5v6h-10"/>
      <circle cx="10" cy="26" r="2.5"/>
      <circle cx="27" cy="26" r="2.5"/>
      <path d="M10 16l3 3 5-5"/>
      <path d="M1 14h3M2 19h2"/>
    </svg>
  </div>

  <div class="feature" style="left:44px">
    <div class="feature__title">Easy, Risk-free<br>Savings</div>
    <p class="feature__text">Put your shipments up for bid via LoopLane's simple API integration and receive a response in less than a second. You only use our real-time rates when we beat your contracted rate. No downside. No commitments necessary</p>
  </div>
  <div class="feature-divider" style="left:223px"></div>
  <div class="feature" style="left:242px">
    <div class="feature__title">A Green Parcel is a<br>Cheap Parcel</div>
    <p class="feature__text">When a carrier is already serving an address, they can underbid other carriers for the next package, since they have already paid for that stop. This lowers shipping costs, reduces the number of duplicate stops, and cuts carbon emissions.</p>
  </div>
  <div class="feature-divider" style="left:418px"></div>
  <div class="feature" style="left:434px">
    <div class="feature__title">Quickly Validate<br>Savings</div>
    <p class="feature__text">Connect with us to run a back-test on your shipping data, and see exactly how much money you would've saved on each parcel if you'd used LoopLane for the past 3 months.</p>
  </div>

  <div class="footer-band"></div>
</section>

</body>
</html>
```